MRHT Needs Fundraiser Dinner Invite!!

The Marisol Hendrick Trust, a 501 3(c) non for profit has a yearly fundraiser, with varying themes. Last year it was "cowboys" and "cowgirls"
This year, it is Club Orchid, or 70's disco music. I have uploaded last years invite for reference, some stock photography for inspiration. You are not limited to using the stock photos.

Annual MRHT Fundraiser Dinner
October 13th, 2022
Starts: 6:30pm
RSVP By: September 20th
Place: The Bramwell
Price: $135 per ticket

Target Market(s)

Donors, Business People, Every person

Industry/Entity Type

Non for Profit

Font styles to use
Sans Serif

Colors
0054AA
0677BA
7BADD7
CADEEF
E8F1F8
E54698
E96AAD
F1A4CE
F9D9EA
FCEFF6
6B429C
8869AF
B7A5CE
E3DAEB
F3F0F8

Requirements
Must have
• The invite should be 5x7, be sophisticated as the clientele are mainly business people that come to support the cause. It should be fun and inviting at the same time.

```html
<!DOCTYPE html>
<html lang="en">
<head>
<meta charset="utf-8">
<title>Let's get Groovy — Annual MRHT Fundraiser Dinner</title>
<link rel="stylesheet" href="https://fonts.googleapis.com/css2?family=Shrikhand&family=Cormorant+SC:wght@600;700&display=swap">
<style>
  :root {
    --pink: #E54698;
    --white: #FFFFFF;
    --silver-light: #E4E1E3;
    --silver-mid: #A9A4A8;
    --silver-dark: #4A474B;
    --paper: #FFFFFF;
  }
  html, body {
    margin: 0;
    padding: 0;
    width: 862px;
    height: 1200px;
    overflow: hidden;
    background: var(--paper);
  }
  .invite {
    position: relative;
    width: 862px;
    height: 1200px;
    background: var(--paper);
  }
  .invite__hero {
    position: absolute;
    left: 8px;
    top: 8px;
    width: 846px;
    height: 491px;
    background:
      radial-gradient(circle at 20% 30%, var(--silver-light) 0%, var(--silver-mid) 25%, transparent 45%),
      radial-gradient(circle at 62% 18%, var(--silver-light) 0%, var(--silver-mid) 22%, transparent 42%),
      radial-gradient(circle at 85% 55%, var(--silver-light) 0%, var(--silver-mid) 22%, transparent 42%),
      radial-gradient(circle at 40% 85%, var(--silver-light) 0%, var(--silver-mid) 22%, transparent 42%),
      linear-gradient(135deg, var(--silver-mid), var(--silver-dark));
  }
  .invite__panel {
    position: absolute;
    left: 8px;
    top: 499px;
    width: 846px;
    height: 693px;
    background: var(--pink);
  }
  .invite__art {
    position: absolute;
    inset: 0;
  }
  .headline {
    font-family: 'Shrikhand', cursive;
    fill: var(--pink);
    stroke: var(--white);
    stroke-width: 8px;
    stroke-linejoin: round;
    paint-order: stroke fill;
  }
  .script {
    font-family: 'Shrikhand', cursive;
    fill: var(--white);
    text-anchor: middle;
  }
  .caps {
    font-family: 'Cormorant SC', serif;
    font-weight: 700;
    fill: var(--white);
    text-anchor: middle;
  }
</style>
</head>
<body>
<main class="invite">
  <div class="invite__hero" role="img" aria-label="Close-up photograph of a pile of silver mirrored disco balls"></div>
  <div class="invite__panel"></div>

  <svg class="invite__art" width="862" height="1200" viewBox="0 0 862 1200">
    <g class="title">
      <text class="headline" x="54" y="206" font-size="104" transform="rotate(-4 54 206)">Let’s</text>
      <text class="headline" x="140" y="292" font-size="58" transform="rotate(-4 140 292)">get</text>
      <text class="headline" x="252" y="414" font-size="148">Groovy</text>
    </g>

    <g class="details">
      <text class="caps" x="431" y="587" font-size="30" letter-spacing="3">annual mrht fundraiser dinner</text>
      <text class="script" x="431" y="690" font-size="44">Thursday</text>
      <text class="caps" x="431" y="748" font-size="38" letter-spacing="5">oct | 13 | 2022</text>
      <text class="script" x="431" y="801" font-size="28">doors open by 6:30pm</text>
      <text class="script" x="431" y="922" font-size="62">The Bramwell</text>
      <text class="script" x="431" y="1000" font-size="36">$135 per ticket</text>
      <text class="script" x="431" y="1090" font-size="36">RSVP</text>
      <text class="caps" x="431" y="1144" font-size="28" letter-spacing="4">sept | 20| 2022</text>
    </g>
  </svg>
</main>
</body>
</html>
```